Korvex Systems*

Stationary design including business cards, letter heads, envelops and email signatures using our new logo

Target Market(s)

Innovative Technologies

Industry/Entity Type

Defense Contracting

Font styles to use
Sans Serif

```html
<!DOCTYPE html>
<html lang="en">
<head>
<meta charset="utf-8">
<title>Korvex Systems – Business Card</title>
<link href="https://fonts.googleapis.com/css2?family=Oswald:wght@400;500&family=Work+Sans:wght@400;500&display=swap" rel="stylesheet">
<style>
  :root {
    --backdrop: #141414;
    --card: #222222;
    --card-edge: #2c2c2c;
    --silver: #b9b9b9;
    --silver-soft: #9a9a9a;
  }
  * { margin: 0; padding: 0; box-sizing: border-box; }
  html, body {
    width: 1200px;
    height: 900px;
    overflow: hidden;
    background: var(--backdrop);
  }
  .stage {
    width: 1200px;
    height: 900px;
    display: flex;
    flex-direction: column;
    align-items: center;
    justify-content: center;
    gap: 40px;
  }
  .card {
    width: 700px;
    height: 400px;
    background: linear-gradient(135deg, var(--card) 0%, #262626 60%, var(--card-edge) 100%);
    position: relative;
    color: var(--silver);
  }
  .card-front {
    display: flex;
    flex-direction: column;
    align-items: center;
    justify-content: center;
  }
  .brand-square {
    width: 34px;
    height: 34px;
    border: 2px solid var(--silver);
    margin-bottom: 26px;
  }
  .brand-name {
    font-family: "Oswald", sans-serif;
    font-weight: 500;
    font-size: 46px;
    letter-spacing: 1px;
    line-height: 1;
    text-transform: uppercase;
    color: var(--silver);
  }
  .brand-tagline {
    margin-top: 8px;
    font-family: "Work Sans", sans-serif;
    font-weight: 500;
    font-size: 9px;
    letter-spacing: 5px;
    text-transform: uppercase;
    color: var(--silver-soft);
  }
  .card-back {
    display: flex;
    align-items: center;
    justify-content: center;
  }
  .holder {
    text-align: right;
    padding-right: 34px;
  }
  .holder-name {
    font-family: "Oswald", sans-serif;
    font-weight: 500;
    font-size: 38px;
    letter-spacing: 2px;
    line-height: 1.1;
    text-transform: uppercase;
  }
  .holder-role {
    font-family: "Work Sans", sans-serif;
    font-size: 18px;
    letter-spacing: 1px;
    color: var(--silver-soft);
  }
  .divider {
    width: 2px;
    height: 130px;
    background: var(--silver-soft);
  }
  .contact {
    padding-left: 34px;
    font-family: "Work Sans", sans-serif;
    font-size: 18px;
    letter-spacing: 1px;
    line-height: 1.45;
    list-style: none;
  }
  .contact-address { margin-bottom: 4px; }
  .contact-line {
    display: flex;
    align-items: center;
    gap: 8px;
  }
  .contact-line svg {
    width: 13px;
    height: 13px;
    flex: none;
    fill: none;
    stroke: var(--silver);
    stroke-width: 1.6;
  }
</style>
</head>
<body>
<main class="stage">
  <section class="card card-front">
    <div class="brand-square"></div>
    <h1 class="brand-name">Korvex Systems</h1>
    <p class="brand-tagline">Innovative Defense Systems</p>
  </section>

  <section class="card card-back">
    <div class="holder">
      <h2 class="holder-name">Daniel Hart</h2>
      <p class="holder-role">Founder</p>
    </div>
    <div class="divider"></div>
    <ul class="contact">
      <li class="contact-address">418 Alder Ridge Road<br>Colville, WA 99114</li>
      <li class="contact-line">
        <svg viewBox="0 0 16 16"><path d="M4 1.5 L6.5 4.5 L5 6.5 Q6.5 9.5 9.5 11 L11.5 9.5 L14.5 12 L12.5 14.5 Q5 13.5 1.5 4 Z"/></svg>
        509 555 0187
      </li>
      <li class="contact-line">
        <svg viewBox="0 0 16 16"><rect x="1.5" y="3.5" width="13" height="9"/><path d="M1.5 3.5 L8 9 L14.5 3.5"/></svg>
        info@korvexsystems.com
      </li>
      <li class="contact-line">
        <svg viewBox="0 0 16 16"><circle cx="8" cy="8" r="6.5"/><ellipse cx="8" cy="8" rx="3" ry="6.5"/><path d="M1.5 8 H14.5"/></svg>
        www.korvexsystems.com
      </li>
    </ul>
  </section>
</main>
</body>
</html>
```